Box Truck Wrap design with images and our logo

We need a design for the side of our box truck. We are an HVAC and Plumbing Company serving commercial and residential markets and want something catchy, not too busy but more than just logos. Maybe some equipment and/or verbiage of what we do. Real images would be a bonus. We want people to recognize our brand, see our story on the side of this tuck, much like a billboard, and be motivated to contact us for service.

Target Market(s)

Residential homeowners who need HVAC and Plumbing Services

Industry/Entity Type

Commercial and Residential HVAC

Font styles to use
Other font styles liked:
• Calibri

Colors
0054AA
0677BA
7BADD7
CADEEF
E8F1F8

Requirements
Must have
• Our logo, visible interpretation of what we do - Here is our website - www.kestrelvaleplumbing.example
Nice to have
• Integrated, easy design
Should not have
• Must not be too busy

```html
<!DOCTYPE html>
<html lang="en">
<head>
<meta charset="utf-8">
<title>Kestrelvale Box Truck Wrap – Side Layouts</title>
<link rel="stylesheet" href="https://fonts.googleapis.com/css2?family=Montserrat:wght@600;800&family=Oswald:wght@500&display=swap">
<style>
  :root {
    --brand-blue: #0054AA;
    --brand-navy: #1b2f6b;
    --band-black: #1f1f23;
    --panel-white: #ffffff;
    --canvas-bg: #E8F1F8;
    --text-white: #ffffff;
    --edge: #CADEEF;
  }
  * { margin: 0; padding: 0; box-sizing: border-box; }
  html, body { width: 1200px; height: 1200px; overflow: hidden; background: var(--canvas-bg); }
  .canvas { position: relative; width: 1200px; height: 1200px; }
  .wrap-layout {
    position: absolute; left: 50px; width: 1100px; height: 540px; overflow: hidden;
  }
  .wrap-layout--straight { top: 30px; }
  .wrap-layout--angled { top: 630px; }
  .wrap-shapes { position: absolute; inset: 0; width: 1100px; height: 540px; }
  .brand-name {
    font-family: "Montserrat", sans-serif; font-weight: 800; color: var(--brand-blue);
    font-size: 92px; line-height: 1; letter-spacing: -1px; white-space: nowrap;
  }
  .brand-trade {
    font-family: "Montserrat", sans-serif; font-weight: 800; color: var(--band-black);
    font-size: 33px; line-height: 1.02; text-align: right; white-space: nowrap;
  }
  .contact-line {
    font-family: "Montserrat", sans-serif; font-weight: 600; color: var(--text-white);
    white-space: nowrap; display: flex; align-items: center; gap: 18px;
  }
  .contact-phone { font-size: 27px; letter-spacing: 3px; }
  .contact-divider { font-size: 30px; font-weight: 400; }
  .contact-web { font-size: 16px; letter-spacing: 1.5px; }
  .service-list {
    font-family: "Oswald", sans-serif; font-weight: 500; color: var(--text-white);
    font-size: 14px; letter-spacing: 0.5px; text-transform: uppercase; line-height: 1.45; white-space: nowrap;
  }
  .service-list span + span::before { content: "·"; margin: 0 8px; }

  /* straight layout */
  .wrap-layout--straight .brand-name { position: absolute; left: 34px; top: 52px; }
  .wrap-layout--straight .brand-trade { position: absolute; right: 340px; top: 150px; }
  .wrap-layout--straight .contact-line { position: absolute; left: 60px; top: 302px; height: 40px; }
  .wrap-layout--straight .service-list { position: absolute; left: 44px; top: 362px; }

  /* angled layout */
  .brand-block-angled {
    position: absolute; left: 46px; top: 30px; width: 700px; height: 230px;
    transform: rotate(11.3deg); transform-origin: 0 0;
  }
  .brand-block-angled .brand-name { position: absolute; left: 0; top: 0; }
  .brand-block-angled .brand-trade { position: absolute; right: 0; top: 98px; }
  .band-copy-angled {
    position: absolute; left: 0; top: 286px; width: 1150px; height: 140px;
    transform: rotate(11.3deg); transform-origin: 0 0;
  }
  .band-copy-angled .contact-line { position: absolute; left: 40px; top: 6px; height: 40px; }
  .band-copy-angled .service-list { position: absolute; left: 48px; top: 58px; }
</style>
</head>
<body>
<main class="canvas">

  <section class="wrap-layout wrap-layout--straight" aria-label="Truck side wrap, straight band layout">
    <svg class="wrap-shapes" viewBox="0 0 1100 540" aria-hidden="true">
      <rect class="box-panel" x="0" y="0" width="820" height="540" rx="12" fill="var(--panel-white)" stroke="var(--edge)"/>
      <path class="cab-panel" d="M834 140 L975 140 L1100 330 L1100 540 L834 540 Z" fill="var(--panel-white)" stroke="var(--edge)"/>
      <path class="blue-field" d="M0 356 L712 356 L780 540 L0 540 Z" fill="var(--brand-blue)"/>
      <path class="black-band" d="M0 300 L700 300 Q732 300 746 334 L820 520 L792 520 L720 348 L0 348 Z" fill="var(--band-black)"/>
    </svg>
    <div class="brand-name">Kestrelvale</div>
    <div class="brand-trade">PLUMBING HEATING<br>&amp; AIR CONDITIONING</div>
    <div class="contact-line">
      <span class="contact-phone">(555) 014-2297</span>
      <span class="contact-divider">|</span>
      <span class="contact-web">www.kestrelvaleplumbing.example</span>
    </div>
    <div class="service-list">
      <div><span>Residential Air Conditioning</span><span>Residential Heating</span><span>Indoor Air Quality</span><span>Residential Plumbing</span></div>
      <div><span>Commercial Air Conditioning</span><span>Commercial Heating</span><span>Commercial Plumbing</span><span>Garage Heaters</span></div>
    </div>
  </section>

  <section class="wrap-layout wrap-layout--angled" aria-label="Truck side wrap, angled band layout">
    <svg class="wrap-shapes" viewBox="0 0 1100 540" aria-hidden="true">
      <rect class="box-panel" x="0" y="0" width="820" height="540" rx="12" fill="var(--panel-white)" stroke="var(--edge)"/>
      <path class="cab-panel" d="M834 140 L975 140 L1100 330 L1100 540 L834 540 Z" fill="var(--panel-white)" stroke="var(--edge)"/>
      <path class="blue-field" d="M0 331 L1100 551 L1100 540 L0 540 Z" fill="var(--brand-blue)"/>
      <path class="blue-field" d="M0 336 L1100 556 L1100 540 L0 540 Z" fill="var(--brand-blue)"/>
      <path class="blue-field-body" d="M0 336 L820 500 L820 540 L0 540 Z" fill="var(--brand-blue)"/>
      <path class="black-band" d="M0 286 L1100 506 L1100 551 L0 331 Z" fill="var(--band-black)"/>
      <path class="blue-field-cab" d="M834 503 L1100 556 L1100 540 L834 540 Z" fill="var(--brand-blue)"/>
    </svg>
    <div class="brand-block-angled">
      <div class="brand-name">Kestrelvale</div>
      <div class="brand-trade">PLUMBING HEATING<br>&amp; AIR CONDITIONING</div>
    </div>
    <div class="band-copy-angled">
      <div class="contact-line">
        <span class="contact-phone">(555) 014-2297</span>
        <span class="contact-divider">|</span>
        <span class="contact-web">www.kestrelvaleplumbing.example</span>
      </div>
      <div class="service-list">
        <div><span>Residential Air Conditioning</span><span>Residential Heating</span><span>Indoor Air Quality</span><span>Residential Plumbing</span></div>
        <div><span>Commercial Air Conditioning</span><span>Commercial Heating</span><span>Commercial Plumbing</span><span>Garage Heaters</span></div>
      </div>
    </div>
  </section>

</main>
</body>
</html>
```